E-Book for Independent Filmmakers. Looking for a simple design with a Human Figure, gazing at the sky, and a Shooting Star in background. Bonus Points if there's a Cinema camera on a tripod next to him. Current placeholder cover attached
(I don't own photo).

Target Market(s)

18 - 42

Industry/Entity Type

Film Production

Font styles to use
Sans Serif

Colors
1b1b1b
5c5c5c
b1b1b1

Requirements
Must have
• Simplicity, Elegance.
• LEAP PAST THE HORIZON
Nice to have
• Would be Awesome to experiment with 2 Designs, under Title "LEAP PAST THE HORIZON:"
• Subtitle Option 1: The 7 Layers of Modern Moviecraft
• Subtitle Option2: An eBook for Filmmakers
Should not have
• Boringness

```html
<!DOCTYPE html>
<html lang="en">
<head>
<meta charset="utf-8">
<title>Leap Past the Horizon — eBook Cover</title>
<link rel="stylesheet" href="https://fonts.googleapis.com/css2?family=Bebas+Neue&display=swap">
<style>
  :root {
    --backdrop: #d3e1f0;
    --night-deep: #1b1b1b;
    --night-teal: #1d4d58;
    --aurora-teal: #2fa2a6;
    --aurora-blue: #4d60d2;
    --glow: #b8c8ec;
    --ground: #141618;
    --title: #ffffff;
  }
  html, body {
    margin: 0;
    width: 1200px;
    height: 914px;
    overflow: hidden;
    background: var(--backdrop);
  }
  .canvas {
    position: relative;
    width: 1200px;
    height: 914px;
  }
  .cover {
    position: absolute;
    left: 382px;
    top: 158px;
    width: 420px;
    height: 604px;
    overflow: hidden;
  }
  .cover-art {
    position: absolute;
    inset: 0;
    background:
      linear-gradient(to bottom, transparent 0%, transparent 82%, var(--ground) 91%, var(--ground) 100%),
      radial-gradient(ellipse 70% 30% at 65% 70%, var(--glow) 0%, transparent 70%),
      linear-gradient(160deg,
        var(--night-deep) 0%,
        var(--night-teal) 18%,
        var(--aurora-teal) 38%,
        #3a8fb4 55%,
        var(--aurora-blue) 72%,
        #27306a 84%,
        var(--ground) 100%);
  }
  .title {
    position: absolute;
    inset: 0;
    margin: 0;
  }
  .title-art {
    display: block;
    width: 420px;
    height: 604px;
  }
  .title-line {
    font-family: "Bebas Neue", "Oswald", sans-serif;
    font-weight: 400;
    fill: var(--title);
    text-transform: uppercase;
  }
</style>
</head>
<body>
  <main class="canvas">
    <section class="cover">
      <div class="cover-art" role="img" aria-label="Photograph of a starry night sky with a bright shooting star streaking across the upper right and the Milky Way glowing in teal and blue; below the title a lone figure stands silhouetted on a dark hilltop, gazing up at the sky"></div>
      <h1 class="title" aria-label="Leap Past the Horizon">
        <svg class="title-art" viewBox="0 0 420 604" aria-hidden="true">
          <text class="title-line" x="210" y="254" font-size="158" text-anchor="middle" textLength="236" lengthAdjust="spacingAndGlyphs">Leap</text>
          <text class="title-line" x="210" y="334" font-size="84" text-anchor="middle" textLength="236" lengthAdjust="spacingAndGlyphs">Past the</text>
          <text class="title-line" x="210" y="418" font-size="92" text-anchor="middle" textLength="242" lengthAdjust="spacingAndGlyphs">Horizon</text>
        </svg>
      </h1>
    </section>
  </main>
</body>
</html>
```